New Business Card (to reflect updated website content and graphics)

I changed some text and graphics on my website, so I need a new business card.

Target Market(s)

Mostly women, ages 30 - 60.

Industry/Entity Type

Life Coaching

Contact Information for Business Card

Included in attached Word document

Font styles to use
Sans Serif

Requirements
Must have
• I am not a creative person, so I will defer to designer. Take a look at my website, and you can get a feel for me, my style, and my target audience. Thank You!

My 3 branding colors are included in attached Word document.

```html
<!DOCTYPE html>
<html lang="en">
<head>
<meta charset="utf-8">
<title>Heartward Coaching – Business Card</title>
<link rel="stylesheet" href="https://fonts.googleapis.com/css2?family=Poppins:wght@400;600&display=swap">
<style>
  :root {
    --bg: #2b2b2d;
    --teal: #2a94b0;
    --teal-deep: #1f7f9c;
    --coral: #f27c6a;
    --white: #ffffff;
    --ink: #4a4a4a;
  }
  * { box-sizing: border-box; margin: 0; padding: 0; }
  html, body { width: 1200px; height: 880px; overflow: hidden; }
  body {
    background: var(--bg);
    font-family: "Poppins", sans-serif;
    position: relative;
  }
  .card {
    position: absolute;
    width: 680px;
    height: 390px;
    border-radius: 22px;
    overflow: hidden;
  }
  /* Front */
  .card-front {
    left: 80px; top: 50px;
    background: var(--teal);
    display: flex; align-items: center; justify-content: center;
  }
  .brand-name {
    color: var(--white);
    font-weight: 400;
    font-size: 44px;
    letter-spacing: 0.06em;
    display: flex; align-items: center; gap: 18px;
  }
  .brand-dot {
    width: 18px; height: 18px; border-radius: 50%;
    background: var(--white);
  }
  /* Back */
  .card-back {
    left: 440px; top: 450px;
    background: var(--white);
  }
  .word-cloud {
    position: absolute;
    right: 70px; top: 30px;
    width: 230px; height: 200px;
    border-radius: 14px;
    background: linear-gradient(135deg, var(--teal) 0%, var(--teal-deep) 55%, var(--coral) 100%);
    opacity: 0.85;
  }
  .accent-bar {
    position: absolute;
    right: 0; top: 215px;
    width: 22px; height: 60px;
    background: var(--coral);
  }
  .details {
    position: absolute;
    left: 48px; top: 170px;
  }
  .person-name {
    color: var(--teal);
    font-weight: 600;
    font-size: 24px;
    letter-spacing: 0.03em;
    text-transform: uppercase;
  }
  .name-rule {
    width: 190px; height: 3px;
    background: var(--coral);
    margin: 8px 0 12px;
  }
  .titles li {
    list-style: none;
    color: var(--ink);
    font-size: 15px;
    line-height: 1.45;
  }
  .contact { margin-top: 18px; }
  .contact li {
    list-style: none;
    display: flex; align-items: center; gap: 12px;
    color: var(--ink);
    font-size: 15px;
    line-height: 1.6;
  }
  .contact svg { width: 15px; height: 15px; fill: var(--teal); flex: none; }
  .domain { color: var(--teal); }
</style>
</head>
<body>

<section class="card card-front">
  <div class="brand-name"><span class="brand-dot"></span>Heartward Coaching</div>
</section>

<section class="card card-back">
  <div class="word-cloud" role="img" aria-label="Word cloud illustration of coaching themes such as hope, joy, love and peace"></div>
  <div class="accent-bar"></div>

  <div class="details">
    <h1 class="person-name">Marla Devereux</h1>
    <div class="name-rule"></div>
    <ul class="titles">
      <li>Certified Professional Life Coach</li>
      <li>Health &amp; Wellness Coach</li>
      <li>Advanced Grief Renewal Process Specialist</li>
    </ul>
    <ul class="contact">
      <li>
        <svg viewBox="0 0 24 24" aria-hidden="true"><path d="M6.6 10.8a15.1 15.1 0 0 0 6.6 6.6l2.2-2.2c.3-.3.7-.4 1-.2 1.1.4 2.3.6 3.6.6.6 0 1 .4 1 1V20c0 .6-.4 1-1 1C10.6 21 3 13.4 3 4c0-.6.4-1 1-1h3.5c.6 0 1 .4 1 1 0 1.3.2 2.5.6 3.6.1.3 0 .7-.2 1z"/></svg>
        (555) 014-2273
      </li>
      <li>
        <svg viewBox="0 0 24 24" aria-hidden="true"><path d="M2 5h20v14H2z M2 5l10 8 10-8" fill="none" stroke="#2a94b0" stroke-width="2"/></svg>
        marla@heartwardcoaching.com
      </li>
      <li>
        <svg viewBox="0 0 24 24" aria-hidden="true"><circle cx="12" cy="12" r="9" fill="none" stroke="#2a94b0" stroke-width="2"/><path d="M3 12h18M12 3c3 3 3 15 0 18M12 3c-3 3-3 15 0 18" fill="none" stroke="#2a94b0" stroke-width="1.5"/></svg>
        <span>www.<span class="domain">heartwardcoaching</span>.com</span>
      </li>
    </ul>
  </div>
</section>

</body>
</html>
```